Tallbrook Real Estate A5 Flyer

A5 Flyer for print distribution.

Front (include attached photo and branding):
Tallbrook are a new face in the Shelley & Rossmoyne real estate market. The Tallbrook team are both Shelley ‘locals’ and are genuinely and sincerely committed to this community. They put people first and pursue exceptional outcomes for their clients. This is the founding vision of Tallbrook.

Values:
Outstanding Customer Service
Timely Communication
Integrity Always
People First
Exceptional Negotiation

If you’re thinking of selling, interested in a free market appraisal, or simply want to find out more about the Tallbrook team, please reach out to Owen or Rupert for a chat. We’d love to shout you a coffee at The Lantern Coffee + Kitchen.

Tallbrook Real Estate
E: hello@tallbrookrealestate-example.com.au
W: tallbrookrealestate-example.com.au

Back (half the page about Owen, other half the page about Rupert). Please include headshots (Rupert is the younger one):

Rupert Finchley (Property Consultant):

Rupert has an in-depth understanding of all things property & finance related. With a degree in property & finance, diploma in finance & mortgage broking, certificate IV in real estate practice, project management roles in residential property development, plus years of small business experience as co-founder/co-owner of The Lantern Coffee + Kitchen, his experience in managing competing demands and complex scenarios runs far and wide.

Rupert also has experience in corporate negotiations which is proving to be a very beneficial skill set. Rupert is deeply committed to people and pursuing exceptional outcomes for his clients. He has built a reputation as a man of his word who is genuine and sincere and willing to go above and beyond for his clients.

rupert@tallbrookrealestate-example.com.au
0400 318 262

Owen Pritchard (Director / Licensee):

Owen has worked in various roles inclusive of being a Real Estate Agent, Bank Manager, Financial Counsellor, Mortgage Broker, and previously a Commercial Pilot. He spent eight years in remote Western Australia, where he worked for an international mining company creating strategies to help support the well-being of employees. Owen’s focus in life has always been to help people. To him, it is always about the relationship. Owen gets enormous satisfaction from seeing individuals, families, and businesses thrive financially. He has become a skilled negotiator with extensive experience working for a number of corporations and private firms.
 
What differentiates Owen is his compassion and commitment to people. He works hard to be an excellent communicator with the aim of achieving great results. He  has extensive sales experience with incredible ability to push the boundaries, think outside the box and meet or surpass expectations. This is why his clients keep coming back and continue to refer well into the future. 

owen@tallbrookrealestate-example.com.au
0400 627 139

Target Market(s)

House Sellers / House Buyers

Industry/Entity Type

Real Estate

Colors
0054AA
0677BA
7BADD7
CADEEF
E8F1F8

Requirements
Must have
• Branding / logo, river photo, head shots, company details etc
Nice to have
• Design as per attached branding guide

```html
<!DOCTYPE html>
<html lang="en">
<head>
<meta charset="utf-8">
<title>Tallbrook Real Estate – A5 Flyer</title>
<link href="https://fonts.googleapis.com/css2?family=Poppins:wght@400;500;600;700;800&display=swap" rel="stylesheet">
<style>
  :root {
    --stage: #b5c8d7;
    --navy: #10294a;
    --navy-deep: #0c2039;
    --blue: #1a75bb;
    --gold: #9b7431;
    --ink: #2a2f36;
    --white: #ffffff;
    --sky-top: #3f93d6;
    --sky-mid: #a9cdea;
    --sky-light: #dcebf6;
  }
  * { box-sizing: border-box; margin: 0; padding: 0; }
  html, body { width: 789px; height: 1200px; overflow: hidden; }
  body {
    background: var(--stage);
    font-family: "Poppins", sans-serif;
    color: var(--ink);
    position: relative;
  }
  .page {
    position: absolute;
    top: 338px;
    width: 370px;
    height: 524px;
    background: var(--white);
    overflow: hidden;
    box-shadow: 0 4px 14px rgba(20, 40, 60, 0.25);
  }
  .page--front { left: 16px; }
  .page--back { left: 403px; }

  /* brand */
  .brand {
    position: absolute;
    top: 30px;
    left: 0;
    width: 100%;
    display: flex;
    justify-content: center;
    align-items: center;
    gap: 8px;
  }
  .brand__dot { width: 22px; height: 22px; border-radius: 50%; background: var(--navy); }
  .brand__name {
    font-size: 13px;
    font-weight: 400;
    letter-spacing: 5px;
    color: var(--navy);
  }
  .brand--light .brand__dot { background: var(--white); }
  .brand--light .brand__name { color: var(--white); }

  /* front */
  .hero {
    position: absolute;
    left: 0; top: 0;
    width: 100%; height: 363px;
    background: linear-gradient(180deg,
      var(--sky-top) 0%, var(--sky-mid) 22%, var(--sky-light) 38%, #cfe0ee 48%,
      #7f97a8 54%, #4f6b80 64%, #2f4e68 80%, #1b3550 100%);
  }
  .headline {
    position: absolute;
    left: 0; top: 63px;
    width: 100%;
    text-align: center;
    font-weight: 800;
    line-height: 1;
  }
  .headline__lead { display: block; font-size: 21px; color: var(--navy); }
  .headline__place { display: block; font-size: 21px; color: var(--blue); margin-top: 2px; }
  .headline__band {
    display: block;
    margin: 3px auto 0;
    width: 319px;
    height: 23px;
    line-height: 23px;
    background: var(--navy-deep);
    color: var(--white);
    font-size: 15px;
    font-weight: 700;
    letter-spacing: 6px;
  }
  .intro {
    position: absolute;
    left: 50px; top: 145px;
    width: 270px;
    text-align: center;
    font-size: 7px;
    line-height: 8.4px;
    color: var(--ink);
  }
  .values {
    position: absolute;
    left: 26px; top: 343px;
    width: 318px;
    display: flex;
    gap: 4.5px;
  }
  .value {
    position: relative;
    flex: 1;
    height: 54px;
    background: var(--navy);
    border-radius: 3px;
    color: var(--white);
    font-size: 5.8px;
    font-weight: 500;
    line-height: 7px;
    text-align: center;
    padding-top: 21px;
  }
  .value__icon {
    position: absolute;
    left: 50%; top: -11px;
    transform: translateX(-50%);
    width: 22px; height: 22px;
    border-radius: 50%;
    background: var(--white);
    border: 1.5px solid var(--navy);
  }
  .value__icon svg { position: absolute; left: 4px; top: 4px; }
  .values-bracket { position: absolute; left: 0; top: 396px; }
  .values-title {
    position: absolute;
    left: 0; top: 404px;
    width: 100%;
    text-align: center;
    font-size: 18px;
    font-weight: 800;
    color: var(--gold);
  }
  .invite {
    position: absolute;
    left: 23px; top: 444px;
    width: 326px;
    font-size: 7px;
    line-height: 8.4px;
    color: var(--ink);
  }

  /* footer */
  .footer {
    position: absolute;
    left: 0; bottom: 0;
    width: 100%; height: 42px;
    display: flex;
    font-size: 7px;
    font-weight: 500;
    color: var(--white);
  }
  .footer__web, .footer__mail { display: flex; align-items: center; gap: 4px; padding-left: 22px; }
  .footer__web { width: 188px; background: var(--gold); }
  .footer__mail { flex: 1; background: var(--navy-deep); padding-left: 12px; }

  /* back */
  .backdrop {
    position: absolute;
    left: 0; top: 0;
    width: 100%; height: 150px;
    background: linear-gradient(180deg, #1c3756 0%, #132c48 45%, #0e2540 100%);
  }
  .profile-card {
    position: absolute;
    left: 58px; top: 78px;
    width: 289px; height: 147px;
    background: var(--white);
    border-radius: 10px;
    box-shadow: 3px 3px 0 var(--gold);
  }
  .headshot {
    position: absolute;
    width: 92px; height: 105px;
    border-radius: 4px;
    background: linear-gradient(180deg, #e4e6e8 0%, #cfd3d7 55%, #2c3a55 100%);
  }
  .headshot--rupert { left: 26px; top: 95px; }
  .headshot--owen { left: 24px; top: 259px; }
  .profile {
    position: absolute;
    left: 135px;
    width: 204px;
  }
  .profile--rupert { top: 96px; }
  .profile--owen { top: 262px; }
  .profile__name { font-size: 11px; font-weight: 700; color: var(--navy); line-height: 12px; }
  .profile__role { font-size: 4.6px; font-weight: 600; color: var(--navy); margin-top: 1px; }
  .profile__contact {
    display: flex;
    gap: 10px;
    font-size: 5.6px;
    font-weight: 500;
    color: var(--navy);
    margin-top: 5px;
    align-items: center;
  }
  .profile__contact span { display: flex; align-items: center; gap: 2px; }
  .profile__bio { font-size: 5.1px; line-height: 6.3px; margin-top: 6px; color: var(--ink); }
  .profile__bio + .profile__bio { margin-top: 4px; }
  .profile--owen .profile__bio { font-size: 5.3px; line-height: 6.9px; }
  .bio-wide {
    position: absolute;
    left: 43px; top: 386px;
    width: 293px;
    font-size: 5.3px;
    line-height: 6.9px;
    color: var(--ink);
  }
  .owen-bracket { position: absolute; left: 0; top: 0; }
</style>
</head>
<body>

<section class="page page--front">
  <div class="hero" role="img" aria-label="Aerial photo of the Swan River foreshore at Shelley with suburbs and the city skyline under a blue sky"></div>

  <div class="brand">
    <span class="brand__dot"></span>
    <span class="brand__name">TALLBROOK</span>
  </div>

  <h1 class="headline">
    <span class="headline__lead">NEW FACE IN</span>
    <span class="headline__place">THE SHELLEY &amp; ROSSMOYNE</span>
    <span class="headline__band">REAL ESTATE MARKET</span>
  </h1>

  <p class="intro">The Tallbrook team are both Shelley ‘locals’ and are genuinely and sincerely committed to this community. They put people first and pursue exceptional outcomes for their clients. This is the founding vision of Tallbrook.</p>

  <div class="values">
    <div class="value"><span class="value__icon"><svg width="11" height="11" viewBox="0 0 11 11"><circle cx="5.5" cy="3.5" r="2" fill="none" stroke="#9b7431" stroke-width="1"/><path d="M1.5 10c0-2.5 2-4 4-4s4 1.5 4 4" fill="none" stroke="#9b7431" stroke-width="1"/></svg></span>Outstanding<br>Customer<br>Service</div>
    <div class="value"><span class="value__icon"><svg width="11" height="11" viewBox="0 0 11 11"><rect x="1" y="1.5" width="9" height="6" rx="1" fill="none" stroke="#9b7431" stroke-width="1"/><path d="M3 7.5 2.5 10 5 7.5" fill="none" stroke="#9b7431" stroke-width="1"/></svg></span>Timely<br>Communication</div>
    <div class="value"><span class="value__icon"><svg width="11" height="11" viewBox="0 0 11 11"><path d="M2 6l2.5 2.5L9.5 3" fill="none" stroke="#9b7431" stroke-width="1.3"/></svg></span>Integrity<br>Always</div>
    <div class="value"><span class="value__icon"><svg width="11" height="11" viewBox="0 0 11 11"><circle cx="3.5" cy="3" r="1.5" fill="none" stroke="#9b7431" stroke-width="1"/><circle cx="7.5" cy="3" r="1.5" fill="none" stroke="#9b7431" stroke-width="1"/><path d="M1 9.5c0-2 1-3 2.5-3s2.5 1 2.5 3M5 9.5c0-2 1-3 2.5-3s2.5 1 2.5 3" fill="none" stroke="#9b7431" stroke-width="1"/></svg></span>People<br>First</div>
    <div class="value"><span class="value__icon"><svg width="11" height="11" viewBox="0 0 11 11"><path d="M1 6l2.5-2.5h2l3 3-1.5 1.5-3-2" fill="none" stroke="#9b7431" stroke-width="1"/><path d="M10 6 7.5 3.5" fill="none" stroke="#9b7431" stroke-width="1"/></svg></span>Exceptional<br>Negotiation</div>
  </div>

  <svg class="values-bracket" width="370" height="24" viewBox="0 0 370 24" aria-hidden="true">
    <path d="M45 1 V18 Q45 21 48 21 H123 M247 21 H310 Q313 21 313 18 V1" fill="none" stroke="#10294a" stroke-width="0.8" stroke-dasharray="2 1.5"/>
  </svg>
  <h2 class="values-title">OUR VALUES</h2>

  <p class="invite">If you’re thinking of selling, interested in a free market appraisal, or simply want to find out more about the Tallbrook team, please reach out to Owen or Rupert for a chat.&nbsp; We’d love to shout you a coffee at The Lantern Coffee + Kitchen.</p>

  <footer class="footer">
    <div class="footer__web">
      <svg width="7" height="7" viewBox="0 0 10 10" aria-hidden="true"><circle cx="5" cy="5" r="4.3" fill="none" stroke="#fff" stroke-width="1"/><ellipse cx="5" cy="5" rx="2" ry="4.3" fill="none" stroke="#fff" stroke-width="0.8"/><path d="M0.7 5h8.6" stroke="#fff" stroke-width="0.8"/></svg>
      tallbrookrealestate-example.com.au
    </div>
    <div class="footer__mail">
      <svg width="7" height="5" viewBox="0 0 10 7" aria-hidden="true"><rect width="10" height="7" fill="#c99a4b"/><path d="M0 0l5 4 5-4" fill="none" stroke="#fff" stroke-width="0.8"/></svg>
      hello@tallbrookrealestate-example.com.au
    </div>
  </footer>
</section>

<section class="page page--back">
  <div class="backdrop" role="img" aria-label="Dusk aerial photo of the river and city skyline"></div>

  <div class="brand brand--light">
    <span class="brand__dot"></span>
    <span class="brand__name">TALLBROOK</span>
  </div>

  <div class="profile-card"></div>
  <div class="headshot headshot--rupert" role="img" aria-label="Headshot of Rupert Finchley in a navy suit"></div>
  <article class="profile profile--rupert">
    <h3 class="profile__name">RUPERT FINCHLEY</h3>
    <p class="profile__role">PROPERTY CONSULTANT</p>
    <p class="profile__contact">
      <span><svg width="6" height="6" viewBox="0 0 10 10" aria-hidden="true"><path d="M2 0.5l2 2.5-1 1.5c.8 1.5 1.5 2.2 3 3l1.5-1 2.5 2-1.5 1.5C4.5 10 0 5.5 0.5 2z" fill="#9b7431"/></svg>0400 318 262</span>
      <span><svg width="6" height="4.5" viewBox="0 0 10 7" aria-hidden="true"><rect width="10" height="7" fill="#9b7431"/><path d="M0 0l5 4 5-4" fill="none" stroke="#fff" stroke-width="0.8"/></svg>rupert@tallbrookrealestate-example.com.au</span>
    </p>
    <p class="profile__bio">Rupert has an in-depth understanding of all things property &amp; finance related. With a degree in property &amp; finance, diploma in finance &amp; mortgage broking, certificate IV in real estate practice, project management roles in residential property development, plus years of small business experience as co-founder/co-owner of The Lantern Coffee + Kitchen, his experience in managing competing demands and complex scenarios runs far and wide.</p>
    <p class="profile__bio">Rupert also has experience in corporate negotiations which is proving to be a very beneficial skill set. Rupert is deeply committed to people and pursuing exceptional outcomes for his clients. He has built a reputation as a man of his word who is genuine and sincere and willing to go above and beyond for his clients.</p>
  </article>

  <svg class="owen-bracket" width="370" height="470" viewBox="0 0 370 470" aria-hidden="true">
    <path d="M348 290 V438 Q348 449 337 449 H52 Q41 449 41 440" fill="none" stroke="#9b7431" stroke-width="2.5"/>
  </svg>
  <div class="headshot headshot--owen" role="img" aria-label="Headshot of Owen Pritchard in a navy suit and striped tie"></div>
  <article class="profile profile--owen">
    <h3 class="profile__name">OWEN PRITCHARD</h3>
    <p class="profile__role">DIRECTOR / LICENSEE</p>
    <p class="profile__contact">
      <span><svg width="6" height="6" viewBox="0 0 10 10" aria-hidden="true"><path d="M2 0.5l2 2.5-1 1.5c.8 1.5 1.5 2.2 3 3l1.5-1 2.5 2-1.5 1.5C4.5 10 0 5.5 0.5 2z" fill="#9b7431"/></svg>0400 627 139</span>
      <span><svg width="6" height="4.5" viewBox="0 0 10 7" aria-hidden="true"><rect width="10" height="7" fill="#9b7431"/><path d="M0 0l5 4 5-4" fill="none" stroke="#fff" stroke-width="0.8"/></svg>owen@tallbrookrealestate-example.com.au</span>
    </p>
    <p class="profile__bio">Owen has worked in various roles inclusive of being a Real Estate Agent, Bank Manager, Financial Counsellor, Mortgage Broker, and previously a Commercial Pilot. He spent eight years in remote Western Australia, where he worked for an international mining company creating strategies to help support the well-being of employees. Owen’s focus in life has always been to help people. To him, it is always about the relationship. Owen gets enormous satisfaction from seeing individuals, families, and businesses thrive financially. He has become a skilled negotiator with extensive experience working for a number of corporations and private firms.</p>
  </article>
  <p class="bio-wide">What differentiates Owen is his compassion and commitment to people. He works hard to be an excellent communicator with the aim of achieving great results. He has extensive sales experience with incredible ability to push the boundaries, think outside the box and meet or surpass expectations. This is why his clients keep coming back and continue to refer well into the future.</p>

  <footer class="footer">
    <div class="footer__web">
      <svg width="7" height="7" viewBox="0 0 10 10" aria-hidden="true"><circle cx="5" cy="5" r="4.3" fill="none" stroke="#fff" stroke-width="1"/><ellipse cx="5" cy="5" rx="2" ry="4.3" fill="none" stroke="#fff" stroke-width="0.8"/><path d="M0.7 5h8.6" stroke="#fff" stroke-width="0.8"/></svg>
      tallbrookrealestate-example.com.au
    </div>
    <div class="footer__mail">
      <svg width="7" height="5" viewBox="0 0 10 7" aria-hidden="true"><rect width="10" height="7" fill="#c99a4b"/><path d="M0 0l5 4 5-4" fill="none" stroke="#fff" stroke-width="0.8"/></svg>
      hello@tallbrookrealestate-example.com.au
    </div>
  </footer>
</section>

</body>
</html>
```